Company director needs a business card design

I am a semi-retired former senior finance executive who sits on a number of public and private company boards and do some consulting work. I work largely with emerging businesses but deal regularly with top end of town lawyers, bankers etc. I need a thoughtful but relatively conservative design which would also resonate with my younger client base. Some colour would be good. Information limited to name, address, office tel, mobile and email.

Industry/Entity Type

Finance

```html
<!DOCTYPE html>
<html lang="en">
<head>
<meta charset="utf-8">
<title>Daniel Whitford – Business Cards</title>
<link rel="stylesheet" href="https://fonts.googleapis.com/css2?family=Cinzel:wght@400;700&display=swap">
<style>
  :root {
    --backdrop: #333333;
    --card: #141516;
    --silver-light: #e4e4e4;
    --silver-dark: #8d8d8d;
    --silver-text: #a9a9a9;
    --gold-light: #e6c65c;
    --gold-dark: #a8761f;
    --gold-text: #c49a3a;
  }
  * { margin: 0; padding: 0; box-sizing: border-box; }
  html, body {
    width: 1200px;
    height: 700px;
    overflow: hidden;
    background: var(--backdrop);
  }
  .stage {
    position: relative;
    width: 1200px;
    height: 700px;
  }
  .card {
    position: absolute;
    width: 525px;
    height: 299px;
    background: var(--card);
    font-family: 'Cinzel', serif;
  }
  .card--silver { left: 54px; top: 199px; }
  .card--gold { left: 624px; top: 201px; }

  .card__name {
    position: absolute;
    right: 30px;
    top: 31px;
    font-size: 15.5px;
    font-weight: 700;
    letter-spacing: 0.3px;
    -webkit-background-clip: text;
    background-clip: text;
    color: transparent;
  }
  .card--silver .card__name {
    background-image: linear-gradient(90deg, var(--silver-light), var(--silver-dark));
  }
  .card--gold .card__name {
    background-image: linear-gradient(90deg, var(--gold-dark), var(--gold-light) 55%, var(--gold-dark));
  }

  .card__details {
    position: absolute;
    left: 33px;
    top: 181px;
    font-size: 12.5px;
    line-height: 15.3px;
  }
  .card--gold .card__details { top: 177px; }
  .card--silver .card__details { color: var(--silver-text); }
  .card--gold .card__details { color: var(--gold-text); }

  .card__address { margin-bottom: 17px; }
  .card__contact p, .card__address p { white-space: nowrap; }
  .card__email { text-transform: uppercase; font-size: 11.5px; }
</style>
</head>
<body>
<main class="stage">
  <section class="card card--silver">
    <h1 class="card__name">Daniel Whitford</h1>
    <div class="card__details">
      <div class="card__address">
        <p>48 Carrow Avenue,</p>
        <p>Balmoral NSW 2088</p>
      </div>
      <div class="card__contact">
        <p>02 9461 2835</p>
        <p>0422 518 704</p>
        <p class="card__email">daniel_whitford@kestrel.net.au</p>
      </div>
    </div>
  </section>

  <section class="card card--gold">
    <h1 class="card__name">Daniel Whitford</h1>
    <div class="card__details">
      <div class="card__address">
        <p>48 Carrow Avenue,</p>
        <p>Balmoral NSW 2088</p>
      </div>
      <div class="card__contact">
        <p>02 9461 2835</p>
        <p>0422 518 704</p>
        <p class="card__email">daniel_whitford@kestrel.net.au</p>
      </div>
    </div>
  </section>
</main>
</body>
</html>
```